Revamp of business card

i need to revamp my business card to look more modern and neat

Contact Information for Business Card

details provided in pdf file, text will change

```html
<!DOCTYPE html>
<html lang="en">
<head>
<meta charset="utf-8">
<title>Huemark Business Card</title>
<link href="https://fonts.googleapis.com/css2?family=Montserrat:wght@400;600;700&display=swap" rel="stylesheet">
<style>
  :root {
    --page: #2f2f2f;
    --card: #ececeb;
    --brand: #d4460f;
    --ink: #1f1f1f;
    --white: #ffffff;
  }
  * { margin: 0; padding: 0; box-sizing: border-box; }
  html, body { width: 1200px; height: 1000px; overflow: hidden; }
  body {
    background: var(--page);
    font-family: "Montserrat", Arial, sans-serif;
    position: relative;
  }
  .card {
    position: absolute;
    left: 228px;
    width: 744px;
    height: 455px;
    background: var(--card);
    overflow: hidden;
  }
  .card--front { top: 36px; }
  .card--back { top: 509px; }
  .abs { position: absolute; white-space: nowrap; }

  /* Front */
  .brand-mark {
    top: 46px; right: 34px;
    display: flex; align-items: center; gap: 8px;
    color: var(--brand); font-weight: 700; font-size: 40px; line-height: 1;
  }
  .brand-mark .dot { width: 12px; height: 12px; border-radius: 50%; background: var(--brand); }
  .person-name { left: 40px; top: 118px; font-size: 45px; line-height: 1; color: var(--brand); font-weight: 400; }
  .person-name strong { font-weight: 700; }
  .person-role { left: 41px; top: 169px; font-size: 21px; line-height: 1; color: var(--brand); }
  .divider { position: absolute; left: 41px; top: 228px; width: 41px; height: 7px; background: var(--brand); }
  .contact { left: 41px; font-size: 18px; line-height: 20px; color: var(--brand); display: flex; }
  .contact .label { width: 34px; font-weight: 700; }
  .contact--phone { top: 272px; }
  .contact--email { top: 327px; }
  .contact--address { top: 364px; }
  .footer-rule { position: absolute; top: 426px; height: 7px; background: var(--brand); }
  .footer-rule--long { left: 0; width: 500px; }
  .footer-rule--short { left: 718px; width: 26px; }
  .footer-url { left: 510px; top: 419px; font-size: 17px; line-height: 20px; font-weight: 700; color: var(--brand); }

  /* Back */
  .side-band { position: absolute; left: 0; top: 0; width: 132px; height: 455px; background: var(--brand); }
  .badge {
    left: 23px; top: 32px; width: 84px; height: 84px; border-radius: 50%;
    background: var(--white); display: flex; align-items: center; justify-content: center;
    color: var(--brand); font-weight: 700; font-size: 15px;
  }
  .social-icon { background: var(--white); }
  .social-icon--circle { left: 36px; top: 192px; width: 60px; height: 60px; border-radius: 50%; }
  .social-icon--square { left: 39px; top: 348px; width: 54px; height: 54px; border-radius: 10px; }
  .social-handle { width: 132px; left: 0; text-align: center; font-size: 12px; font-weight: 700; color: var(--white); line-height: 14px; }
  .social-handle--fb { top: 259px; }
  .social-handle--ig { top: 408px; }
  .service-title { left: 198px; font-size: 22px; line-height: 26px; font-weight: 700; color: var(--brand); }
  .service-text { left: 198px; font-size: 16px; line-height: 22px; color: var(--ink); }
</style>
</head>
<body>

<section class="card card--front" aria-label="Business card front">
  <div class="abs brand-mark"><span class="dot"></span>Huemark</div>
  <h1 class="abs person-name"><strong>Dorian</strong> Vale</h1>
  <p class="abs person-role">Director</p>
  <span class="divider"></span>
  <div class="abs contact contact--phone"><span class="label">P :</span><span>0400 118 372,<br>08 7100 2655</span></div>
  <div class="abs contact contact--email"><span class="label">E :</span><span>vale@huemark.com.au</span></div>
  <div class="abs contact contact--address"><span class="label">A :</span><span>Shop 4, 18-24 Harbour Lane,<br>Meridian Arcade, Adelaide 5000</span></div>
  <span class="footer-rule footer-rule--long"></span>
  <span class="abs footer-url">www.huemark.com.au</span>
  <span class="footer-rule footer-rule--short"></span>
</section>

<section class="card card--back" aria-label="Business card back">
  <div class="side-band"></div>
  <div class="abs badge">Huemark</div>
  <span class="abs social-icon social-icon--circle"></span>
  <span class="abs social-handle social-handle--fb">huemarkaustralia</span>
  <span class="abs social-icon social-icon--square"></span>
  <span class="abs social-handle social-handle--ig">huemark</span>

  <h2 class="abs service-title" style="top:50px">Tshirt Prints &amp; Embroidery</h2>
  <p class="abs service-text" style="top:83px">Prints on all kinds of apparel and fabrics<br>www.tessaweave.com.au<br>www.loomfield.com.au<br>www.coastthreads.com.au<br>www.kindleapparel.com.au</p>

  <h2 class="abs service-title" style="top:211px">Prints on Promotional and Giveaways</h2>
  <p class="abs service-text" style="top:243px">Mugs, Caps, KeyChains, Name Tags, Wall Clocks etc.</p>

  <h2 class="abs service-title" style="top:282px">Prints and Design Services</h2>
  <p class="abs service-text" style="top:315px">Bussiness Cards, Flyers, Brochures, Posters, Banners etc.</p>

  <h2 class="abs service-title" style="top:353px">Photo Prints</h2>
  <p class="abs service-text" style="top:382px">HD Metal prints to photographic paper prints</p>
</section>

</body>
</html>
```